New Dental Office Needs an Attractive and user friendly Website Designed

I need a website for a new dental office. The Name is Maplecrest Dentistry. I would like a Modern design with a user friendly interface and usability.
I would like a landing page, a page that lists the services we offer: Cosmetic Dentistry, Implants, Dental Hygiene, Emergency Services, Restorations, Dentures
Target Market(s)
Mid to upper class
Industry/Entity Type
Dentistry
Coding
Coded - Design and coding required
Number of Pages Required
1 page
Requirements
Must have
- Landing page that has a scheduling option, Procedures, operating hours, and contact us info
Nice to have
- Appealing design, Soft comforting colors. Easy to navigate page, Modern and professional.

```html
<!DOCTYPE html>
<html lang="en">
<head>
<meta charset="utf-8">
<title>Maplecrest Dentistry</title>
<link href="https://fonts.googleapis.com/css2?family=Urbanist:wght@400;500;600;700&display=swap" rel="stylesheet">
<style>
:root{
  --blue:#1aa5ea;
  --cyan:#dcf5fd;
  --cyan-2:#bfe9fa;
  --ink:#161616;
  --muted:#4a4a4a;
  --line:#e2e2e2;
  --soft:#f5f5f5;
  --footer:#2a2a2a;
  --white:#fff;
}
*{box-sizing:border-box;margin:0;padding:0}
html,body{width:1200px;height:4008px;overflow:hidden}
body{position:relative;background:var(--white);font-family:"Urbanist",sans-serif;color:var(--ink)}
.abs{position:absolute}
.photo{position:absolute;border-radius:22px;overflow:hidden}
.btn{position:absolute;display:flex;align-items:center;justify-content:center;border-radius:6px;font-size:13px;font-weight:600;color:var(--white)}
.btn-blue{background:var(--blue)}
.btn-dark{background:var(--ink)}
.arrow-circle{position:absolute;width:28px;height:28px;border:1.6px solid var(--ink);border-radius:50%;display:flex;align-items:center;justify-content:center}
.arrow-circle svg{width:14px;height:14px}
.logo{font-size:21px;font-weight:700;color:var(--ink);white-space:nowrap}
.nav-link{position:absolute;top:26px;font-size:13px;font-weight:500}
.hero-title{left:193px;top:110px;font-size:38px;font-weight:700;line-height:1.22;white-space:nowrap;letter-spacing:-0.3px}
.hero-text{left:193px;top:222px;width:420px;font-size:12.5px;line-height:1.75;color:var(--muted)}
.hero-card{position:absolute;background:var(--cyan);border-radius:18px}
.hero-card h3{position:absolute;left:19px;top:18px;font-size:21px;font-weight:500;line-height:1.35;width:190px}
.illus{position:absolute;border-radius:12px}
.section-title{position:absolute;left:0;width:1200px;text-align:center;font-size:31px;font-weight:600}
.section-sub{position:absolute;left:320px;width:560px;text-align:center;font-size:12.5px;line-height:1.75;color:var(--muted)}
.svc{position:absolute;border-radius:14px;overflow:hidden}
.svc-plain{background:var(--soft);border:1.5px solid var(--line)}
.svc-cyan{background:var(--cyan);border:1.5px solid var(--cyan-2)}
.svc h3{position:absolute;left:19px;top:18px;font-size:25px;font-weight:500;line-height:1.2}
.svc-photo h3{color:var(--white)}
.svc-photo p{position:absolute;left:19px;top:62px;width:230px;font-size:12px;line-height:1.3;color:var(--white)}
.reasons-title{left:608px;top:1222px;font-size:31px;font-weight:600;line-height:1.2;white-space:nowrap}
.feature{position:absolute;display:flex;align-items:center;gap:12px;font-size:15px;font-weight:500}
.feature i{width:28px;height:28px;border-radius:50%;display:block}
.steps-title{left:199px;top:1570px;font-size:31px;font-weight:600}
.steps-sub{left:199px;top:1622px;width:620px;font-size:13px;line-height:1.6;color:var(--muted)}
.vlabel{position:absolute;writing-mode:vertical-rl;transform:rotate(180deg);font-size:25px;color:#a9a9a9;font-weight:400}
.cta-band{left:193px;top:2180px;width:814px;height:247px;background:var(--cyan);border-radius:16px}
.cta-title{left:218px;top:2204px;font-size:31px;font-weight:600;line-height:1.4}
.hours{position:absolute;font-size:11px;font-weight:700}
.hours span{color:var(--blue);font-weight:600;margin-left:12px}
.quote-card{left:255px;top:2571px;width:688px;height:375px;border:1.5px solid var(--line);border-radius:22px;background:var(--white)}
.quote{left:340px;top:2712px;width:520px;text-align:center;font-size:14px;line-height:1.8;color:#2a2a2a}
.nav-arrow{position:absolute;width:50px;height:50px;border-radius:50%;display:flex;align-items:center;justify-content:center}
.form-card{left:608px;top:3022px;width:399px;height:342px;border:1.5px solid var(--line);border-radius:16px}
.field{position:absolute;background:var(--soft);border:1px solid var(--line);border-radius:6px;font-size:11px;color:#555;display:flex;align-items:center;padding-left:12px;gap:8px}
.field i{width:12px;height:11px;background:#b7b7b7;border-radius:2px;display:block}
.contact{position:absolute;top:3440px;width:240px;height:116px;border:1.5px solid var(--line);border-radius:14px}
.contact .ic{position:absolute;left:18px;top:22px;width:40px;height:36px;background:#e5e5e5;border-radius:6px}
.contact h4{position:absolute;left:18px;top:72px;font-size:21px;font-weight:500}
.contact .go{position:absolute;right:-2px;top:-2px;width:42px;height:40px;background:var(--ink);border-radius:8px;display:flex;align-items:center;justify-content:center;box-shadow:0 0 0 6px var(--white)}
.footer{left:0;top:3632px;width:1200px;height:376px;background:var(--footer);color:var(--white)}
.f-text{position:absolute;font-size:11.5px;color:#ddd;line-height:1.6}
.f-head{position:absolute;font-size:14px;font-weight:600}
.f-link{position:absolute;font-size:12px;color:#e6e6e6}
</style>
</head>
<body>

<div class="abs logo" style="left:193px;top:20px">Maplecrest Dentistry</div>
<a class="nav-link" style="left:443px">Home</a>
<a class="nav-link" style="left:505px">About Us</a>
<a class="nav-link" style="left:585px">Service</a>
<a class="nav-link" style="left:655px">Scheduling</a>
<a class="nav-link" style="left:745px">Contact</a>
<div class="btn btn-blue" style="left:938px;top:19px;width:69px;height:31px;font-size:11px">Book Now</div>

<h1 class="abs hero-title">Shaping Beautiful Smiles<br>with Gentle Expertise!</h1>
<p class="abs hero-text">Brighten your smile with personalized dental care. Our experienced team provides gentle, expert treatments to ensure your comfort, confidence, and long-lasting oral health.</p>
<div class="btn btn-blue" style="left:193px;top:302px;width:121px;height:36px;font-size:12px;font-weight:500">Book Appointment</div>
<div class="abs" style="left:331px;top:304px;width:78px;height:34px">
  <div class="abs" role="img" aria-label="Satisfied client portrait" style="left:0;top:0;width:34px;height:34px;border-radius:50%;background:#c9a58c;border:2px solid #fff"></div>
  <div class="abs" role="img" aria-label="Satisfied client portrait" style="left:22px;top:0;width:34px;height:34px;border-radius:50%;background:#9b6b58;border:2px solid #fff"></div>
  <div class="abs" role="img" aria-label="Satisfied client portrait" style="left:44px;top:0;width:34px;height:34px;border-radius:50%;background:#5a4a44;border:2px solid #fff"></div>
</div>
<div class="abs" style="left:414px;top:306px;font-size:11px;line-height:1.4">+50.00<br>Satisfied Clients</div>

<div class="hero-card" style="left:193px;top:426px;width:218px;height:158px">
  <h3>Free Vibrant Dental Checkup</h3>
  <div class="illus" role="img" aria-label="Dental model of teeth and gums" style="left:120px;top:72px;width:82px;height:72px;background:linear-gradient(160deg,#fff 0%,#f2b8ad 60%,#e88f83 100%)"></div>
  <div class="arrow-circle" style="left:22px;top:111px;width:26px;height:26px"><svg viewBox="0 0 14 14"><path d="M4 10 10 4M5 4h5v5" fill="none" stroke="#161616" stroke-width="1.5"/></svg></div>
</div>
<div class="hero-card" style="left:426px;top:364px;width:218px;height:220px">
  <h3>Dental Implant Checkup</h3>
  <div class="illus" role="img" aria-label="Tooth model with toothbrush" style="left:96px;top:84px;width:100px;height:120px;background:linear-gradient(170deg,#fff 0%,#e9edf2 60%,#9fd9a8 100%)"></div>
  <div class="arrow-circle" style="left:22px;top:173px;width:26px;height:26px"><svg viewBox="0 0 14 14"><path d="M4 10 10 4M5 4h5v5" fill="none" stroke="#161616" stroke-width="1.5"/></svg></div>
</div>
<div class="photo" role="img" aria-label="Smiling patient during a dental checkup" style="left:658px;top:100px;width:349px;height:484px;background:linear-gradient(160deg,#d9dde3 0%,#b9a8d6 35%,#c98c6a 60%,#9fdcf0 100%)"></div>

<h2 class="section-title" style="top:658px">Comprehensive dental services</h2>
<p class="section-sub" style="top:710px">We provide complete dental care, from routine cleanings to advanced treatments, ensuring healthy, confident smiles for patients of all ages.</p>

<div class="svc svc-photo" role="img" aria-label="Row of porcelain tooth shade samples" style="left:193px;top:776px;width:342px;height:156px;background:linear-gradient(180deg,#3a2620 0%,#6b4a3c 55%,#d9cbb3 100%)">
  <h3>Cosmetic Dentistry</h3>
  <p>Enhance your smile with safe, modern treatments tailored for beauty and confidence.</p>
</div>
<div class="svc svc-plain" style="left:551px;top:776px;width:219px;height:156px">
  <h3>Teeth<br>Implants</h3>
  <div class="arrow-circle" style="left:172px;top:107px"><svg viewBox="0 0 14 14"><path d="M4 10 10 4M5 4h5v5" fill="none" stroke="#161616" stroke-width="1.5"/></svg></div>
</div>
<div class="svc svc-cyan" style="left:786px;top:776px;width:221px;height:156px">
  <h3>Emergency<br>Care</h3>
  <div class="arrow-circle" style="left:174px;top:107px"><svg viewBox="0 0 14 14"><path d="M4 10 10 4M5 4h5v5" fill="none" stroke="#161616" stroke-width="1.5"/></svg></div>
</div>
<div class="svc svc-plain" style="left:193px;top:948px;width:219px;height:157px">
  <h3>Teeth<br>Restorations</h3>
  <div class="arrow-circle" style="left:172px;top:108px"><svg viewBox="0 0 14 14"><path d="M3 7h8M8 4l3 3-3 3" fill="none" stroke="#161616" stroke-width="1.5"/></svg></div>
</div>
<div class="svc svc-cyan" style="left:428px;top:948px;width:221px;height:157px">
  <h3>Dental<br>Hygiene</h3>
  <div class="arrow-circle" style="left:174px;top:108px"><svg viewBox="0 0 14 14"><path d="M4 10 10 4M5 4h5v5" fill="none" stroke="#161616" stroke-width="1.5"/></svg></div>
</div>
<div class="svc svc-photo" role="img" aria-label="Dentist treating a patient in the clinic" style="left:664px;top:948px;width:343px;height:157px;background:linear-gradient(120deg,#6f6f6f 0%,#4d5a66 50%,#8aa5b8 100%)">
  <h3>Dentures</h3>
  <p>Comfortable, natural-looking dentures designed to restore your smile and chewing ability.</p>
</div>

<div class="photo" role="img" aria-label="Dentist examining a smiling patient in the chair" style="left:208px;top:1180px;width:355px;height:312px;background:linear-gradient(150deg,#e6e6e6 0%,#7aa5c8 35%,#d9a27e 60%,#2f4a6b 100%)"></div>
<div class="abs" style="left:511px;top:1170px;width:62px;height:140px;background:#fff;border-radius:0 0 0 18px"></div>
<div class="abs" role="img" aria-label="Tooth with sparkle illustration" style="left:520px;top:1236px;width:40px;height:40px;border-radius:10px;background:linear-gradient(160deg,#fff,#f3e6b5)"></div>
<div class="abs" style="left:200px;top:1400px;width:111px;height:100px;background:#fff;border-radius:0 18px 0 0"></div>
<div class="abs" style="left:208px;top:1400px;width:103px;height:92px;background:#f6f6f6;border-radius:14px"></div>
<div class="abs" style="left:218px;top:1446px;font-size:14px;font-weight:700">98%</div>
<div class="abs" style="left:218px;top:1468px;font-size:9.5px;font-weight:500">Patient Satisfaction</div>
<svg class="abs" style="left:262px;top:1412px" width="38" height="34" viewBox="0 0 38 34"><circle cx="13" cy="12" r="6" fill="none" stroke="#bbb" stroke-width="1.6"/><path d="M3 32c0-7 4-11 10-11s10 4 10 11" fill="none" stroke="#bbb" stroke-width="1.6"/><circle cx="28" cy="9" r="5" fill="none" stroke="#bbb" stroke-width="1.6"/></svg>

<h2 class="abs reasons-title">Reasons Patients Choose<br>Our Practice</h2>
<div class="feature" style="left:608px;top:1315px"><i style="background:#ece4fb"></i>Gentle Care</div>
<div class="feature" style="left:792px;top:1315px"><i style="background:#dff1fd"></i>Modern Tech</div>
<div class="feature" style="left:608px;top:1363px"><i style="background:#e3f6e6"></i>Family-Friendly</div>
<div class="feature" style="left:792px;top:1363px"><i style="background:#fde4e4"></i>Flexible Scheduling</div>
<div class="btn btn-dark" style="left:608px;top:1413px;width:122px;height:34px;font-size:12px;font-weight:500">Book Appointment</div>

<h2 class="abs steps-title">Your Smile Journey in 3 Easy Steps</h2>
<p class="abs steps-sub">Discover how simple and stress-free dental care can be. From booking to treatment, we make every step easy and comfortable.</p>
<svg class="abs" style="left:199px;top:1846px" width="24" height="22" viewBox="0 0 24 22"><rect x="1" y="3" width="17" height="17" rx="2" fill="#161616"/><rect x="4" y="0" width="3" height="5" fill="#161616"/><rect x="12" y="0" width="3" height="5" fill="#161616"/><circle cx="18" cy="16" r="5" fill="#fff" stroke="#161616" stroke-width="2"/></svg>
<div class="abs" style="left:199px;top:1878px;font-size:19px;font-weight:600">Schedule Your Visit</div>
<p class="abs" style="left:199px;top:1910px;width:270px;font-size:11px;line-height:1.6;color:var(--muted)">Book your appointment online or by phone. Our team will help you find a convenient time that fits your schedule perfectly.</p>
<div class="photo" role="img" aria-label="Happy patient in the chair with a dentist taking notes" style="left:489px;top:1685px;width:395px;height:274px;background:linear-gradient(130deg,#c9b5a6 0%,#e8e6e3 45%,#f4f4f4 70%,#cfd4da 100%)"></div>
<div class="abs" style="left:700px;top:1884px;width:190px;height:80px;background:#fff;border-radius:20px 0 0 0"></div>
<div class="abs" style="left:726px;top:1904px;font-size:22px;font-weight:600">01</div>
<div class="abs" style="left:726px;top:1936px;font-size:19px;font-weight:500">Schedule Your Visit</div>
<svg class="abs" style="left:909px;top:1692px" width="16" height="22" viewBox="0 0 16 22"><path d="M8 21V2M2 8l6-6 6 6" fill="none" stroke="#aaa" stroke-width="1.5"/></svg>
<div class="vlabel" style="left:903px;top:1750px">02 Meet Your Dentist</div>
<svg class="abs" style="left:980px;top:1692px" width="16" height="22" viewBox="0 0 16 22"><path d="M8 21V2M2 8l6-6 6 6" fill="none" stroke="#aaa" stroke-width="1.5"/></svg>
<div class="vlabel" style="left:974px;top:1740px">03 Expert Dental Care</div>

<div class="abs cta-band"></div>
<svg class="abs" style="left:193px;top:2180px" width="814" height="247" viewBox="0 0 814 247"><path d="M400 247C430 140 520 90 640 90L814 90V247Z" fill="#a9defa"/><circle cx="372" cy="92" r="22" fill="none" stroke="#a9defa" stroke-width="10"/></svg>
<div class="abs" role="img" aria-label="Two smiling dentists in white coats" style="left:622px;top:2038px;width:312px;height:389px;border-radius:120px 120px 0 0;background:linear-gradient(180deg,#8a6a55 0%,#f4f6f8 30%,#dfe6ee 70%,#4f6c8f 100%)"></div>
<h2 class="abs cta-title">Stay Ahead of Time<br>Schedule Early!</h2>
<div class="btn btn-dark" style="left:218px;top:2303px;width:101px;height:32px;font-size:10px;font-weight:500">Book Appointment</div>
<div class="hours" style="left:206px;top:2372px">Monday - Friday<span>9 AM - 7 PM</span></div>
<div class="hours" style="left:373px;top:2372px">Saturday - Sunday<span>9 AM - 12 PM</span></div>

<h2 class="section-title" style="top:2515px">What Our Clients&nbsp; Say</h2>
<div class="abs quote-card"></div>
<div class="abs" style="left:232px;top:2734px;width:50px;height:70px;background:#fff"></div>
<div class="abs" style="left:916px;top:2734px;width:50px;height:70px;background:#fff"></div>
<div class="abs" role="img" aria-label="Client portrait" style="left:550px;top:2596px;width:94px;height:94px;border-radius:50%;background:linear-gradient(160deg,#3b2b22,#8a6650)"></div>
<div class="abs" style="left:624px;top:2670px;width:20px;height:20px;border-radius:50%;background:#f6b400;border:2px solid #fff"></div>
<p class="abs quote">The dental website features a clean and professional design that builds trust and credibility with visitors. Its intuitive navigation allows users to easily explore services and book appointments without hassle. High-quality visuals paired with clear call-to-actions create a seamless and engaging user experience throughout the site.</p>
<div class="abs" style="left:0;top:2850px;width:1200px;text-align:center;font-size:25px;font-weight:600">- Nora Whitfield -</div>
<div class="abs" style="left:0;top:2894px;width:1200px;text-align:center;font-size:14px">Marketing Coordinator</div>
<div class="nav-arrow" style="left:224px;top:2743px;border:2px solid #161616"><svg width="20" height="20" viewBox="0 0 20 20"><path d="M15 15 5 5M5 12V5h7" fill="none" stroke="#161616" stroke-width="2"/></svg></div>
<div class="nav-arrow" style="left:929px;top:2745px;background:var(--blue)"><svg width="20" height="20" viewBox="0 0 20 20"><path d="M5 15 15 5M8 5h7v7" fill="none" stroke="#fff" stroke-width="2"/></svg></div>

<div class="photo" role="img" aria-label="Smiling woman having her teeth examined" style="left:193px;top:3022px;width:398px;height:342px;border-radius:16px;background:linear-gradient(130deg,#b9c6d2 0%,#d6a48a 40%,#3e6fb8 75%,#26466e 100%)"></div>
<div class="abs form-card"></div>
<div class="abs" style="left:608px;top:3040px;width:399px;text-align:center;font-size:23px;font-weight:600">Schedule Online</div>
<div class="field" style="left:624px;top:3078px;width:366px;height:37px"><i></i>Name</div>
<div class="field" style="left:624px;top:3128px;width:366px;height:37px"><i></i>Email Address</div>
<div class="field" style="left:624px;top:3179px;width:176px;height:36px"><i></i>Select Date<svg style="position:absolute;right:10px" width="9" height="5"><path d="M0 0h9L4.5 5z" fill="#888"/></svg></div>
<div class="field" style="left:814px;top:3179px;width:176px;height:36px"><i></i>Select Time<svg style="position:absolute;right:10px" width="9" height="5"><path d="M0 0h9L4.5 5z" fill="#888"/></svg></div>
<div class="field" style="left:624px;top:3229px;width:366px;height:64px;align-items:flex-start;padding-top:12px">Explain Problem</div>
<div class="btn btn-dark" style="left:733px;top:3310px;width:151px;height:35px;font-size:12px;font-weight:500">Book Appointment Now</div>

<div class="contact" style="left:208px"><div class="ic"></div><h4>Book Appointment</h4><div class="go"><svg width="14" height="14" viewBox="0 0 14 14"><path d="M3 11 11 3M5 3h6v6" fill="none" stroke="#fff" stroke-width="1.8"/></svg></div></div>
<div class="contact" style="left:479px"><div class="ic"></div><h4>Schedule Call</h4><div class="go"><svg width="14" height="14" viewBox="0 0 14 14"><path d="M3 11 11 3M5 3h6v6" fill="none" stroke="#fff" stroke-width="1.8"/></svg></div></div>
<div class="contact" style="left:750px"><div class="ic"></div><h4>Send Mail</h4><div class="go"><svg width="14" height="14" viewBox="0 0 14 14"><path d="M3 11 11 3M5 3h6v6" fill="none" stroke="#fff" stroke-width="1.8"/></svg></div></div>

<footer class="abs footer">
  <div class="abs logo" style="left:193px;top:40px;color:#fff">Maplecrest Dentistry</div>
  <p class="f-text" style="left:193px;top:80px;width:280px">Creating confident smiles with gentle care, advanced technology, and personalized dental solutions.</p>
  <div class="f-head" style="left:680px;top:76px">Phone Number</div>
  <div class="f-text" style="left:680px;top:100px">+61 2 5550 1287</div>
  <div class="f-head" style="left:873px;top:76px">Email</div>
  <div class="f-text" style="left:873px;top:100px">hello@maplecrestdental.com</div>
  <div class="abs" style="left:193px;top:140px;width:814px;height:1px;background:#444"></div>
  <div class="abs" style="left:599px;top:140px;width:1px;height:82px;background:#444"></div>
  <div class="f-head" style="left:193px;top:160px">Opening Hours</div>
  <div class="f-text" style="left:193px;top:188px">Monday - Friday&nbsp;&nbsp;&nbsp;<span style="color:var(--blue)">9 AM - 7 PM</span>&nbsp;&nbsp;&nbsp;&nbsp;-&nbsp;&nbsp;&nbsp;&nbsp;Saturday - Sunday&nbsp;&nbsp;&nbsp;<span style="color:var(--blue)">9 AM - 12 PM</span></div>
  <div class="f-head" style="left:625px;top:160px">Address</div>
  <div class="f-text" style="left:625px;top:188px">18 Elmwood Lane, Harbourview NSW 2000, Australia</div>
  <a class="f-link" style="left:364px;top:256px">Home</a>
  <a class="f-link" style="left:448px;top:256px">About Us</a>
  <a class="f-link" style="left:549px;top:256px">Service</a>
  <a class="f-link" style="left:642px;top:256px">Why Choose Us</a>
  <a class="f-link" style="left:779px;top:256px">Procedure</a>
  <a class="f-link" style="left:457px;top:290px">Our Dentist</a>
  <a class="f-link" style="left:571px;top:290px">Testimonials</a>
  <a class="f-link" style="left:691px;top:290px">Schedule</a>
  <div class="abs" style="left:0;top:346px;width:1200px;text-align:center;font-size:11px;color:#ddd">Copyright © 2025. Maplecrest Dentistry All Rights Reserved.</div>
</footer>

</body>
</html>
```